Lumo Ket

Need business cards designed. Project is an Arts Center in Hollywood. It'll include 3 live theatre, a restaurant and event space.

Target Market(s)

Across the board, young and old.

Industry/Entity Type

Entertainment

Contact Information for Business Card

Be creative. This is a creative venture that I'm building.

```html
<!DOCTYPE html>
<html lang="en">
<head>
<meta charset="utf-8">
<title>Lumo Ket — Business Cards</title>
<link href="https://fonts.googleapis.com/css2?family=Jost:wght@300;400;500;700&display=swap" rel="stylesheet">
<style>
  :root {
    --backdrop: #161616;
    --card: #2a2a2a;
    --gold: #eebd4b;
    --ink-soft: #c9c9c9;
    --icon-bg: #1b1b1b;
    --mark-grey: #4a4a4a;
  }
  html, body {
    margin: 0;
    padding: 0;
    width: 1200px;
    height: 854px;
    overflow: hidden;
    background: var(--backdrop);
    font-family: "Jost", sans-serif;
  }
  .canvas {
    position: relative;
    width: 1200px;
    height: 854px;
  }
  .card {
    position: absolute;
    left: 333px;
    width: 523px;
    background: var(--card);
    box-shadow: 0 6px 18px rgba(0,0,0,0.55);
  }
  .card--front { top: 112px; height: 293px; }
  .card--back { top: 443px; height: 295px; }

  .accent-line {
    position: absolute;
    left: 256px;
    width: 231px;
    height: 4px;
    background: var(--gold);
  }
  .accent-line--top { top: 0; }
  .accent-line--bottom { bottom: 0; left: 254px; }

  .brand {
    position: absolute;
    display: flex;
    align-items: center;
    gap: 10px;
  }
  .brand__dot {
    width: 34px;
    height: 34px;
    border-radius: 50%;
    background: var(--mark-grey);
    flex: none;
  }
  .brand__name {
    color: var(--gold);
    font-weight: 500;
    font-size: 22px;
    letter-spacing: 0.5px;
    white-space: nowrap;
  }
  .card--front .brand { left: 48px; top: 130px; }
  .card--back .brand { left: 50%; top: 85px; transform: translateX(-50%); }

  .person__name {
    position: absolute;
    left: 254px;
    top: 40px;
    margin: 0;
    color: var(--gold);
    font-weight: 300;
    font-size: 31px;
    letter-spacing: 1.5px;
    line-height: 1;
  }
  .person__role {
    position: absolute;
    left: 256px;
    top: 84px;
    margin: 0;
    color: var(--ink-soft);
    font-size: 12px;
    font-weight: 400;
    letter-spacing: 3.2px;
  }

  .contact-list {
    position: absolute;
    left: 253px;
    top: 138px;
    margin: 0;
    padding: 0;
    list-style: none;
  }
  .contact-list__item {
    display: flex;
    align-items: center;
    height: 24px;
    margin-bottom: 10px;
    color: var(--ink-soft);
    font-size: 10.5px;
    letter-spacing: 1.2px;
  }
  .contact-list__icon {
    width: 24px;
    height: 24px;
    margin-right: 16px;
    flex: none;
  }

  .venue__title {
    position: absolute;
    left: 0;
    right: 0;
    top: 152px;
    margin: 0;
    text-align: center;
    color: var(--gold);
    font-weight: 700;
    font-size: 34px;
    line-height: 1;
  }
  .venue__tagline {
    position: absolute;
    left: 0;
    right: 0;
    top: 200px;
    margin: 0;
    text-align: center;
    color: var(--ink-soft);
    font-size: 13.5px;
    letter-spacing: 2px;
  }
</style>
</head>
<body>
<main class="canvas">

  <section class="card card--front" aria-label="Business card front">
    <span class="accent-line accent-line--top"></span>

    <div class="brand">
      <span class="brand__dot"></span>
      <span class="brand__name">Lumo Ket</span>
    </div>

    <h1 class="person__name">Mara Venn</h1>
    <p class="person__role">CREATIVE DIRECTOR</p>

    <ul class="contact-list">
      <li class="contact-list__item">
        <svg class="contact-list__icon" viewBox="0 0 24 24" aria-hidden="true">
          <circle cx="12" cy="12" r="12" fill="var(--icon-bg)"/>
          <path d="M8.4 6.6l1.6-.5 1.3 2.6-1 1c.5 1.3 1.5 2.3 2.8 2.9l1-1 2.6 1.3-.5 1.6c-.3.8-1.2 1.1-2 .9-3-1-5.4-3.3-6.3-6.3-.3-.9.1-1.7.5-2.5z" fill="var(--gold)"/>
        </svg>
        555.014.2290
      </li>
      <li class="contact-list__item">
        <svg class="contact-list__icon" viewBox="0 0 24 24" aria-hidden="true">
          <circle cx="12" cy="12" r="12" fill="var(--icon-bg)"/>
          <g fill="none" stroke="var(--gold)" stroke-width="1.1">
            <circle cx="12" cy="12" r="6"/>
            <ellipse cx="12" cy="12" rx="2.6" ry="6"/>
            <line x1="6" y1="12" x2="18" y2="12"/>
            <line x1="7" y1="9" x2="17" y2="9"/>
            <line x1="7" y1="15" x2="17" y2="15"/>
          </g>
        </svg>
        mvenn@lumoket.test
      </li>
      <li class="contact-list__item">
        <svg class="contact-list__icon" viewBox="0 0 24 24" aria-hidden="true">
          <circle cx="12" cy="12" r="12" fill="var(--icon-bg)"/>
          <path d="M12 5.5a4 4 0 0 1 4 4c0 3-4 8-4 8s-4-5-4-8a4 4 0 0 1 4-4z" fill="var(--gold)"/>
          <circle cx="12" cy="9.5" r="1.5" fill="var(--icon-bg)"/>
        </svg>
        412 Larkmoor Ave
      </li>
    </ul>

    <span class="accent-line accent-line--bottom"></span>
  </section>

  <section class="card card--back" aria-label="Business card back">
    <div class="brand">
      <span class="brand__dot"></span>
      <span class="brand__name">Lumo Ket</span>
    </div>
    <h2 class="venue__title">Arts Center</h2>
    <p class="venue__tagline">Theatre, Restaurant and Event space</p>
  </section>

</main>
</body>
</html>
```